Finish off design for Tool Retailer- One Page Brochure site

We have started work on our tool shop sit but need to to get finished. Just a One page WP that needs tidying up and made to look better and complete.
We also need to be able upload specials and monthly catalogs.
More info in the brief
Target Market(s)
Trades, mines, industiral
Coding
Coded - Design and coding required
Number of Pages Required
1 page
Font styles to use
Sans Serif
Requirements
Must have
- Please see brief
Nice to have
- Please see brief
Should not have
- Please see brief

```html
<!DOCTYPE html>
<html lang="en">
<head>
<meta charset="utf-8">
<title>Ridgeline Tools</title>
<link href="https://fonts.googleapis.com/css2?family=Open+Sans:wght@400;600;700&family=Roboto+Condensed:wght@400;700&display=swap" rel="stylesheet">
<style>
:root{
  --red:#c8202e;
  --red-dark:#a51a25;
  --ink:#262626;
  --panel:#2b2b2b;
  --footer:#2a2a2a;
  --bar:#1c1c1c;
  --light:#eeeeee;
  --line:#dddddd;
  --text:#555555;
  --white:#ffffff;
}
*{box-sizing:border-box;margin:0;padding:0}
html,body{width:1200px;height:3770px;overflow:hidden}
body{font-family:"Open Sans",Arial,sans-serif;color:var(--text);background:var(--white);position:relative}
.abs{position:absolute}
.heading{font-family:"Roboto Condensed",Arial,sans-serif;font-weight:700;color:var(--ink)}
.section-title{position:absolute;left:0;width:1200px;text-align:center;font-family:"Roboto Condensed",Arial,sans-serif;font-weight:700;font-size:34px;color:var(--ink)}
.section-title::after{content:"";display:block;width:60px;height:4px;background:var(--red);margin:14px auto 0}
.section-title.light{color:var(--white)}
.section-title.light::after{background:var(--white)}

/* top bar */
.top-bar{left:0;top:0;width:1200px;height:31px;background:var(--bar);color:#ccc;font-size:12px}
.top-bar .account{position:absolute;right:180px;top:8px;display:flex;gap:22px}
.top-bar .account span::before{content:"";display:inline-block;width:9px;height:9px;border:1px solid #ccc;border-radius:2px;margin-right:6px;vertical-align:-1px}

/* header */
.site-header{left:0;top:31px;width:1200px;height:114px;background:var(--red)}
.brand{position:absolute;left:173px;top:34px;display:flex;align-items:center;gap:12px;color:var(--white);font-family:"Roboto Condensed",Arial,sans-serif;font-weight:700;font-size:34px;letter-spacing:1px}
.brand .mark{width:30px;height:30px;background:var(--white)}
.subscribe{position:absolute;left:565px;top:18px;color:var(--white);font-size:13px}
.subscribe .form{display:flex;margin-top:12px}
.subscribe .field{width:386px;height:34px;background:var(--white);border-radius:17px 0 0 17px;font-size:12px;color:#999;padding:9px 18px}
.subscribe .btn{width:86px;height:34px;background:var(--ink);color:var(--white);font-size:11px;font-weight:700;border-radius:0 17px 17px 0;text-align:center;line-height:34px}

/* nav */
.main-nav{left:0;top:145px;width:1200px;height:50px;background:var(--white);border-bottom:1px solid var(--line)}
.main-nav ul{list-style:none;display:flex;gap:36px;position:absolute;left:182px;top:16px;font-size:13px;font-weight:700;color:var(--ink)}

/* hero */
.hero{left:0;top:195px;width:1200px;height:417px}
.hero .photo{position:absolute;inset:0;background:linear-gradient(90deg,#1a1a1a 0%,#3a3634 45%,#2a2625 100%)}
.hero h1{position:absolute;left:85px;top:152px;font-family:"Roboto Condensed",Arial,sans-serif;font-weight:700;font-size:50px;line-height:1.25;color:var(--red);text-transform:uppercase}
.hero h1 span{display:block;color:var(--white);font-weight:400}
.hero p{position:absolute;left:85px;top:292px;width:460px;font-size:16px;line-height:1.45;color:#e6e6e6}

/* specials */
.specials{left:173px;top:782px;width:854px;height:506px}
.tile{position:absolute;overflow:hidden}
.tile.dark{background:var(--ink)}
.tile.light{background:var(--light)}
.tile .img{position:absolute}
.tile h3{position:absolute;font-family:"Roboto Condensed",Arial,sans-serif;font-weight:700;font-size:20px}
.tile.dark h3{color:var(--white)}
.tile.light h3{color:var(--ink)}
.tile p{position:absolute;font-size:11px;line-height:1.4;color:#cfcfcf}

/* features */
.feature{position:absolute;top:1338px;height:219px;border:1px solid var(--line);text-align:center;background:var(--white)}
.feature .icon{width:58px;height:58px;margin:28px auto 16px;border-radius:50%;border:2px solid var(--red);display:flex;align-items:center;justify-content:center}
.feature h4{font-size:13px;font-weight:700;color:var(--ink)}
.feature p{font-size:11px;line-height:1.5;margin:10px 26px 0;text-align:left;color:#777}

/* catalogue */
.catalogue{left:0;top:1627px;width:1200px;height:555px;background:var(--red)}
.catalogue .img{position:absolute;left:173px;top:203px;width:581px;height:305px;background:linear-gradient(135deg,#d9742f 0%,#3b3b3b 45%,#c4d23a 100%);opacity:.9}
.catalogue h3{position:absolute;left:807px;top:248px;width:240px;font-family:"Roboto Condensed",Arial,sans-serif;font-weight:700;font-size:22px;line-height:1.35;color:var(--white)}
.catalogue p{position:absolute;left:807px;top:330px;width:230px;font-size:12px;line-height:1.5;color:#f3d4d6}
.catalogue .button{position:absolute;left:807px;top:417px;width:115px;height:34px;border:2px solid var(--white);color:var(--white);font-size:11px;font-weight:700;text-align:center;line-height:30px}

/* about */
.about-photo{left:173px;top:2377px;width:408px;height:254px;background:linear-gradient(180deg,#8fa6c4 0%,#b8c4cf 45%,#6e5a4e 70%,#5e5e5e 100%)}
.about-text{left:612px;top:2385px;width:415px;font-size:12px;line-height:1.55}
.about-text .lead{color:var(--red);font-weight:700;font-size:13px;margin-bottom:14px}
.about-text p+p{margin-top:14px}

/* contact */
.map{left:0;top:2820px;width:1200px;height:499px;background:linear-gradient(90deg,#e8eef2 0%,#eef1ec 40%,#f2f0ea 100%)}
.contact-form{left:173px;top:2820px;width:424px;height:408px;background:var(--panel);padding:28px 40px}
.contact-form .input{height:34px;border:1px solid #666;border-radius:4px;background:#fff;font-size:12px;color:#999;padding:8px 12px;margin-bottom:12px}
.contact-form .input.message{height:150px}
.contact-form .send{height:34px;border-radius:17px;background:var(--red);color:var(--white);font-size:11px;font-weight:700;text-align:center;line-height:34px;margin-top:18px}

/* footer */
.site-footer{left:0;top:3319px;width:1200px;height:418px;background:var(--footer);color:#bbb;font-size:12px}
.site-footer h5{font-family:"Roboto Condensed",Arial,sans-serif;font-weight:700;font-size:19px;color:var(--white);margin-bottom:22px}
.footer-brand{position:absolute;left:173px;top:55px;width:190px}
.footer-brand .name{display:flex;align-items:center;gap:10px;color:var(--white);font-family:"Roboto Condensed",Arial,sans-serif;font-weight:700;font-size:24px;margin-bottom:18px}
.footer-brand .name .mark{width:22px;height:22px;background:var(--red)}
.footer-brand p{line-height:1.5;margin-bottom:20px}
.footer-brand li{list-style:none;display:flex;gap:12px;align-items:flex-start;line-height:1.5;margin-bottom:12px}
.footer-links{position:absolute;left:392px;top:55px}
.footer-links .cols{display:flex;gap:50px}
.footer-links ul{list-style:none;line-height:2.1}
.footer-news{position:absolute;left:612px;top:55px;width:200px}
.footer-news p{line-height:1.5}
.footer-news .field{margin-top:18px;height:30px;background:#444;font-size:11px;padding:7px 12px;color:#999}
.footer-news .btn{margin-top:8px;height:26px;width:200px;background:var(--red);color:var(--white);font-size:11px;font-weight:700;text-align:center;line-height:26px}
.footer-social{position:absolute;left:848px;top:55px}
.footer-social .icons{display:flex;gap:14px}
.footer-social .icons span{width:14px;height:14px;border-radius:50%;background:#ddd}
.copyright{left:0;top:3737px;width:1200px;height:33px;background:var(--bar);color:#999;font-size:11px;padding:10px 173px}
</style>
</head>
<body>

<div class="abs top-bar">
  <div class="account"><span>Login</span><span>Register</span></div>
</div>

<header class="abs site-header">
  <div class="brand"><span class="mark"></span>Ridgeline Tools</div>
  <div class="subscribe">
    Subscribe to our newsletter
    <div class="form"><div class="field">Email...</div><div class="btn">SUBSCRIBE</div></div>
  </div>
</header>

<nav class="abs main-nav">
  <ul><li>Home</li><li>About us</li><li>Specials</li><li>Current Catalogue</li><li>Contact Us</li></ul>
</nav>

<section class="abs hero">
  <div class="photo" role="img" aria-label="Row of red cordless power tools on a dark wooden surface"></div>
  <h1>All Tools<span>For any occasion</span></h1>
  <p>Excepteur sint occaecat cupidatat non proident sunt in culpa qui officia deserunt mollit</p>
</section>

<h2 class="section-title" style="top:664px">Current Specials</h2>

<section class="abs specials">
  <div class="tile dark" style="left:0;top:0;width:414px;height:320px">
    <h3 style="left:22px;top:32px;font-size:32px">Aliquam Quaerat</h3>
    <p style="left:22px;top:82px;width:170px">Quis nostrum exercitationem ullam corporis suscipit laboriosam</p>
    <div class="img" role="img" aria-label="Red corded hammer drill" style="left:190px;top:120px;width:180px;height:170px;background:linear-gradient(135deg,#d8262f,#3a3a3a)"></div>
  </div>
  <div class="tile light" style="left:439px;top:0;width:195px;height:251px">
    <h3 style="left:0;width:195px;text-align:center;top:28px">Qui in Ea Vitae</h3>
    <div class="img" role="img" aria-label="Circular saw" style="left:30px;top:90px;width:135px;height:130px;background:linear-gradient(135deg,#3f7fbf,#9aa3ab)"></div>
  </div>
  <div class="tile dark" style="left:659px;top:0;width:195px;height:320px">
    <div class="img" role="img" aria-label="Green cordless circular saw" style="left:30px;top:20px;width:140px;height:150px;background:linear-gradient(135deg,#3c9a4a,#202020)"></div>
    <h3 style="left:24px;top:240px">Omnis Voluptas</h3>
  </div>
  <div class="tile dark" style="left:439px;top:276px;width:195px;height:230px">
    <h3 style="left:0;width:195px;text-align:center;top:20px">Maiores Alias</h3>
    <div class="img" role="img" aria-label="Yellow and black jobsite radio" style="left:32px;top:80px;width:130px;height:120px;background:linear-gradient(135deg,#f2c21b,#1e1e1e)"></div>
  </div>
  <div class="tile light" style="left:0;top:345px;width:414px;height:161px">
    <h3 style="left:24px;top:60px">Tenetur a Sapiente</h3>
    <div class="img" role="img" aria-label="Rotary laser level on a tripod base" style="left:270px;top:18px;width:120px;height:125px;background:linear-gradient(135deg,#e8b81c,#4a4a4a)"></div>
  </div>
  <div class="tile light" style="left:659px;top:345px;width:195px;height:161px">
    <div class="img" role="img" aria-label="Red portable inflator" style="left:30px;top:16px;width:110px;height:100px;background:linear-gradient(135deg,#c8202e,#2a2a2a)"></div>
    <h3 style="left:24px;top:124px">Duis aute</h3>
  </div>
</section>

<div class="feature" style="left:173px;width:267px">
  <div class="icon"><svg width="28" height="28" viewBox="0 0 28 28"><g fill="none" stroke="#c8202e" stroke-width="2"><circle cx="14" cy="14" r="5"/><path d="M14 3v5M14 20v5M3 14h5M20 14h5M6 6l4 4M18 18l4 4M22 6l-4 4M6 22l4-4"/></g></svg></div>
  <h4>Incredible Design &amp; Functionality</h4>
  <p>Duis autem vel eum iure qui in ea voluptate velit esse quam nihil molestiae consequatur vel illum qui dolorem</p>
</div>
<div class="feature" style="left:465px;width:270px">
  <div class="icon"><svg width="28" height="28" viewBox="0 0 28 28"><g fill="none" stroke="#c8202e" stroke-width="2"><circle cx="14" cy="14" r="10"/><circle cx="14" cy="14" r="4"/></g></svg></div>
  <h4>Awesome Look On Every Devices</h4>
  <p>Duis autem vel eum iure qui in ea voluptate velit esse quam nihil molestiae consequatur vel illum qui dolorem</p>
</div>
<div class="feature" style="left:760px;width:267px">
  <div class="icon"><svg width="28" height="28" viewBox="0 0 28 28"><g fill="#c8202e"><circle cx="14" cy="10" r="5"/><path d="M5 25c0-6 4-9 9-9s9 3 9 9z"/></g></svg></div>
  <h4>Free Support &amp; Updates</h4>
  <p>Duis autem vel eum iure qui in ea voluptate velit esse quam nihil molestiae consequatur vel illum qui dolorem</p>
</div>

<section class="abs catalogue">
  <h2 class="section-title light" style="top:80px">Latest Catalogue</h2>
  <div class="img" role="img" aria-label="Group of measuring meters, laser level and a cordless inflator"></div>
  <h3>Quod maxime placeat facere possimus</h3>
  <p>Temporibus autem quibusdam et aut officiis debitis aut rerum saepe ut et voluptates repudiandae</p>
  <div class="button">DOWNLOAD NOW</div>
</section>

<h2 class="section-title" style="top:2243px">About Us</h2>
<div class="abs about-photo" role="img" aria-label="Street view of the tool shop storefront"></div>
<div class="abs about-text">
  <p class="lead">Our Company started out with an idea to supply and meet the everyday tool needs of people.</p>
  <p>Neque earum rerum hic tenetur a sapiente delectus, ut aut reiciendis voluptatibus maiores alias consequatur aut perferendis doloribus asperiores repellat. Quis nostrum exercitationem ullam corporis et aliquid ex ea commodi consequatur.</p>
  <p>Nemo enim ipsam voluptatem quia voluptas sit aspernatur aut odit aut fugit, sed quia consequuntur magni dolores eos qui ratione voluptatem sequi nesciunt. Neque porro quisquam est, qui dolorem ipsum quia dolor sit amet, consectetur.</p>
</div>

<h2 class="section-title" style="top:2711px">Contact Us</h2>
<div class="abs map" role="img" aria-label="Regional road map with a location pin marking the shop"></div>
<svg class="abs" style="left:822px;top:2968px" width="26" height="36" viewBox="0 0 26 36"><path d="M13 0C6 0 0 6 0 13c0 9 13 23 13 23s13-14 13-23C26 6 20 0 13 0z" fill="#c8202e"/><circle cx="13" cy="13" r="5" fill="#fff"/></svg>
<div class="abs contact-form">
  <div class="input">Name...</div>
  <div class="input">Email...</div>
  <div class="input">Subject....</div>
  <div class="input message">Message....</div>
  <div class="send">SUBMIT</div>
</div>

<footer class="abs site-footer">
  <div class="footer-brand">
    <div class="name"><span class="mark"></span>Ridgeline Tools</div>
    <p>Reprehenderit qui in ea velit esse quam nihil</p>
    <ul>
      <li><svg width="12" height="14" viewBox="0 0 12 14"><path d="M6 0C3 0 0 2.5 0 6c0 4 6 8 6 8s6-4 6-8C12 2.5 9 0 6 0z" fill="#bbb"/></svg>27 Quarry Lane, Stonebridge</li>
      <li><svg width="12" height="12" viewBox="0 0 12 12"><path d="M2 0l3 3-1.5 2a7 7 0 003.5 3.5L9 7l3 3-2 2C5 12 0 7 0 2z" fill="#bbb"/></svg>07 5550 1234</li>
      <li><svg width="12" height="10" viewBox="0 0 12 10"><rect width="12" height="10" fill="#bbb"/><path d="M0 0l6 5 6-5" stroke="#2a2a2a" fill="none"/></svg>hello@ridgelinetools.com</li>
      <li><svg width="12" height="12" viewBox="0 0 12 12"><circle cx="6" cy="6" r="5.5" fill="none" stroke="#bbb"/><path d="M0.5 6h11M6 0.5v11" stroke="#bbb"/></svg>www.ridgelinetools.com</li>
    </ul>
  </div>
  <div class="footer-links">
    <h5>Links</h5>
    <div class="cols">
      <ul><li>Home</li><li>About Us</li><li>Shop</li><li>Catalogue</li></ul>
      <ul><li>Deals</li><li>FAQ</li><li>Blog</li><li>Contact Us</li></ul>
    </div>
  </div>
  <div class="footer-news">
    <h5>Newsletter</h5>
    <p>Subscribe to our newsletter for latest updates</p>
    <div class="field">Email...</div>
    <div class="btn">SUBSCRIBE</div>
  </div>
  <div class="footer-social">
    <h5>Follow Us</h5>
    <div class="icons" aria-label="Social links"><span></span><span></span><span></span><span></span><span></span></div>
  </div>
</footer>

<div class="abs copyright">Copyright © 2018 - Ridgeline Tools - All rights reserved</div>

</body>
</html>
```